Business Card Design

We're a new real estate investment company based out of West Palm Beach Florida. We buy distressed properties to fix and flip. We want the color scheme of the card to match the colors of our logo which is black and gold. We encourage all designers to be creative with the design of the card. We are not looking for a bland, boring, traditional business card. Please use legible fonts for the text as well.

Target Market(s)

Home owners, and Real Estate Investors.

Industry/Entity Type

Real Estate

Contact Information for Business Card

Dalen Vorstagg
Real Estate Investor

ESTATE FALCONS, LLC
7248 S. CORAL HAVEN WAY
SUITE 19
WEST PALM BEACH, FL. 33162
OFFICE: 1-800-555-0182
FAX: 1-888-555-0147
EMAIL: dalen@estatefalcons.example
www.estatefalcons.example

Requirements
Must have
• PLACE THESE WORDS IN BIG BOLD PRINT ON BOTH SIDES OF THE DESIGN:

WE BUY HOUSES WITH CASH!

```html
<!DOCTYPE html>
<html lang="en">
<head>
<meta charset="utf-8">
<title>Estate Falcons Business Card</title>
<link href="https://fonts.googleapis.com/css2?family=Cinzel:wght@400;700;900&family=Tinos:wght@400;700&display=swap" rel="stylesheet">
<style>
  :root {
    --paper: #ffffff;
    --ink: #0b0b0b;
    --card-black: #111111;
    --card-black-edge: #050505;
    --gold-light: #f6e58a;
    --gold-mid: #d9ad2c;
    --gold-deep: #8c6210;
    --gold-faded: #5e5130;
    --suit: #2a2620;
  }
  * { margin: 0; padding: 0; box-sizing: border-box; }
  html, body { width: 800px; height: 1200px; overflow: hidden; background: var(--paper); }
  .sheet { position: relative; width: 800px; height: 1200px; }
  .card {
    position: absolute; left: 133px; width: 535px; height: 307px; overflow: hidden;
    background: radial-gradient(ellipse at 50% 50%, var(--card-black) 0%, var(--card-black-edge) 100%);
  }
  .card--front { top: 226px; height: 306px; }
  .card--back { top: 634px; height: 309px; }
  .card__bands { position: absolute; inset: 0; width: 100%; height: 100%; }
  .brand {
    position: absolute; left: 0; right: 0; display: flex; align-items: center; justify-content: center; gap: 4px;
    font-family: "Cinzel", serif; font-weight: 700; font-size: 7px; color: var(--gold-mid); letter-spacing: 0.5px;
  }
  .brand__dot { width: 14px; height: 14px; border-radius: 50%; background: var(--gold-mid); }
  .card--front .brand { top: 50px; }
  .card--back .brand { top: 233px; }
  .headline {
    position: absolute; left: 60px; width: 400px; top: 126px; text-align: center;
    font-family: "Cinzel", serif; font-weight: 700; font-size: 37px; line-height: 42px; color: var(--ink);
    text-shadow: 2px 3px 3px rgba(0,0,0,0.45);
  }
  .portrait {
    position: absolute; right: 0; top: 96px; width: 88px; height: 210px;
    background: linear-gradient(180deg, rgba(90,70,40,0.55) 0%, var(--suit) 55%, #0e0d0b 100%);
  }
  .ghost {
    position: absolute; left: 0; right: 0; text-align: center;
    font-family: "Cinzel", serif; font-weight: 400; color: var(--gold-faded);
  }
  .ghost--top { top: 6px; font-size: 66px; line-height: 70px; }
  .ghost--bottom { top: 258px; font-size: 35px; line-height: 40px; }
  .identity { position: absolute; left: 0; width: 268px; top: 117px; text-align: center; color: var(--ink); }
  .identity__name, .identity__title { font-family: "Cinzel", serif; font-size: 17px; line-height: 21px; }
  .identity__address { font-family: "Tinos", serif; font-weight: 700; font-size: 6px; line-height: 11px; margin-top: 8px; }
  .contact { position: absolute; left: 272px; top: 122px; font-family: "Tinos", serif; color: var(--ink); }
  .contact__row { display: flex; align-items: center; gap: 2px; white-space: nowrap; }
  .contact__row--phone { font-size: 10.5px; }
  .contact__row--mail { font-size: 8.5px; margin-top: 9px; }
  .contact__icon { width: 15px; height: 11px; }
</style>
</head>
<body>
<div class="sheet">

  <section class="card card--front">
    <svg class="card__bands" viewBox="0 0 535 306" aria-hidden="true">
      <defs>
        <linearGradient id="goldFront" x1="0" y1="0" x2="1" y2="0.3">
          <stop offset="0" stop-color="var(--gold-deep)"/>
          <stop offset="0.3" stop-color="var(--gold-light)"/>
          <stop offset="0.6" stop-color="var(--gold-mid)"/>
          <stop offset="1" stop-color="var(--gold-light)"/>
        </linearGradient>
      </defs>
      <path d="M0 94 Q267 118 535 94 L535 248 Q267 222 0 248 Z" fill="url(#goldFront)"/>
    </svg>
    <div class="brand"><span class="brand__dot"></span>ESTATE FALCONS</div>
    <h1 class="headline">WE BUY HOUSES<br>WITH CASH!</h1>
    <div class="portrait" role="img" aria-label="Portrait photo of the investor in a dark suit"></div>
  </section>

  <section class="card card--back">
    <svg class="card__bands" viewBox="0 0 535 309" aria-hidden="true">
      <defs>
        <linearGradient id="goldBack" x1="0" y1="0" x2="1" y2="0.2">
          <stop offset="0" stop-color="var(--gold-mid)"/>
          <stop offset="0.25" stop-color="var(--gold-light)"/>
          <stop offset="0.5" stop-color="var(--gold-deep)"/>
          <stop offset="0.75" stop-color="var(--gold-light)"/>
          <stop offset="1" stop-color="var(--gold-mid)"/>
        </linearGradient>
      </defs>
      <path d="M0 62 Q267 86 535 62 L535 222 Q267 200 0 222 Z" fill="url(#goldBack)"/>
      <line x1="268" y1="74" x2="268" y2="211" stroke="var(--gold-deep)" stroke-width="1.5"/>
    </svg>
    <div class="ghost ghost--top">WE BUY</div>
    <div class="identity">
      <p class="identity__name">DALEN VORSTAGG</p>
      <p class="identity__title">REAL ESTATE INVESTOR</p>
      <p class="identity__address">ESTATE FALCONS, LLC 7248 S. CORAL HAVEN WAY SUITE 19<br>WEST PALM BEACH, FL. 33162</p>
    </div>
    <div class="contact">
      <p class="contact__row contact__row--phone">
        <svg class="contact__icon" viewBox="0 0 15 11" aria-hidden="true"><rect x="1" y="4" width="13" height="7" rx="1" fill="#fff"/><path d="M0 4 Q7.5 -1 15 4 L12 5 L10 3 L5 3 L3 5 Z" fill="#fff"/><circle cx="7.5" cy="7.5" r="2" fill="var(--ink)"/></svg>
        OFFICE: 1-800-555-0182 FAX: 1-888-555-0147
      </p>
      <p class="contact__row contact__row--mail">
        <svg class="contact__icon" viewBox="0 0 15 11" aria-hidden="true"><rect x="0.5" y="0.5" width="14" height="10" fill="#fff" stroke="#999"/><path d="M0.5 0.5 L7.5 6 L14.5 0.5" fill="none" stroke="#999"/></svg>
        dalen@estatefalcons.example www.estatefalcons.example
      </p>
    </div>
    <div class="brand"><span class="brand__dot"></span>ESTATE FALCONS</div>
    <div class="ghost ghost--bottom">HOUSES WITH CASH!</div>
  </section>

</div>
</body>
</html>
```